Financial Advisor Resource Firm needs business card design

Need business card design for company in Omaha NE called Tallowbrook Partners. We provide resources to financial advisors....workshop programs, retirement analysis, and insurance planning. I would like to see designs that use grays, greens, black, and white colors. The final design should communicate 'collaboration' and be simple yet attractive to financial planning clients. I will attached our logo and another picture of a puzzle piece coming together. I would like the incorporate the puzzle picture somehow, maybe on the back somehow, with color or just the gray scale....OR, the picture be the front of the card with 'Tallowbrook' definition on it (see upload) and then company logo, employee name, title, address on the back (see ppt uploaded). The following disclosure needs to be included somewhere- Advisory services offered through Marlowe Ridge Advisors, LLC.
Updates

I uploaded a svg and ai file of the logo

Target Market(s)

Financial planning clients and financial advisors....so pretty diverse age range of about 40-70.

Industry/Entity Type

Financial Planning

Contact Information for Business Card

Dennis K. Holloway, MBA
Founder/President
5727 E. Larkspur Avenue
Suite 418
Omaha, NE 68297
Phone- (402) 555-0147
Cell- (402) 555-0183
Fax- (402) 555-0129
email- dennis@tallowbrookgroup.example
web address- www.tallowbrookgroup.example

Colors
1b1b1b
474747
d3d3d3
ffffff
9bcb3c
abd036

Requirements
Must have
• Must include logo provided, must be 2 sided, and must have disclosure...all of these items listed in project description

```html
<!DOCTYPE html>
<html lang="en">
<head>
<meta charset="utf-8">
<title>Tallowbrook Partners – Business Card</title>
<link rel="stylesheet" href="https://fonts.googleapis.com/css2?family=Noto+Serif:wght@400;700&family=Roboto:wght@300;400&display=swap">
<style>
  :root {
    --page: #d9d9d9;
    --card-front: #2a2a2a;
    --card-back: #0f0f0f;
    --band: #1b1b1b;
    --green: #8cc63f;
    --white: #ffffff;
    --light: #d3d3d3;
    --muted: #9a9a9a;
  }
  * { box-sizing: border-box; margin: 0; padding: 0; }
  html, body {
    width: 1069px; height: 1200px; overflow: hidden;
    background: var(--page);
  }
  .card {
    position: absolute; left: 75px; width: 924px; height: 528px; overflow: hidden;
  }
  .card--front { top: 62px; background: var(--card-front); }
  .card--back { top: 607px; background: var(--card-back); }

  .front-photo {
    position: absolute; inset: 0;
    background:
      radial-gradient(ellipse 45% 40% at 62% 68%, rgba(120,120,120,.45), transparent 70%),
      radial-gradient(ellipse 30% 50% at 90% 35%, rgba(90,90,90,.4), transparent 70%),
      linear-gradient(160deg, #222 0%, #2c2c2c 45%, #3a3a3a 100%);
  }
  .brand {
    position: absolute; display: flex; align-items: center; gap: 10px;
    font-family: "Roboto", sans-serif; font-weight: 300; color: var(--white);
    text-transform: uppercase; white-space: nowrap;
  }
  .brand__dot { width: 15px; height: 15px; border-radius: 50%; background: var(--green); flex: none; }
  .brand--front { left: 101px; top: 136px; font-size: 35px; letter-spacing: 2px; }
  .brand--back { left: 555px; top: 226px; font-size: 19px; letter-spacing: 1px; gap: 7px; }
  .brand--back .brand__dot { width: 9px; height: 9px; }

  .website {
    position: absolute; left: 0; right: 0; top: 449px; text-align: center;
    font-family: "Roboto", sans-serif; font-weight: 300; font-size: 23px;
    letter-spacing: 3.6px; color: var(--light);
  }

  .person { position: absolute; left: 98px; top: 87px; }
  .person__name {
    font-family: "Noto Serif", serif; font-weight: 700; font-size: 23px;
    letter-spacing: 1.5px; color: var(--green); text-transform: uppercase;
  }
  .person__title {
    margin-top: 6px; font-family: "Noto Serif", serif; font-weight: 400;
    font-size: 22px; letter-spacing: .5px; color: var(--white);
  }

  .contacts { position: absolute; left: 96px; top: 219px; list-style: none; }
  .contacts li {
    display: flex; align-items: center; height: 26px; margin-bottom: 27px;
    font-family: "Roboto", sans-serif; font-weight: 300; font-size: 25px; color: var(--white);
  }
  .contacts li:nth-child(3) { margin-bottom: 19px; }
  .contacts svg { width: 28px; height: 26px; margin-right: 22px; fill: var(--white); flex: none; }

  .address-band {
    position: absolute; left: 0; right: 0; bottom: 0; height: 97px; background: var(--band);
    display: flex; flex-direction: column; align-items: center; justify-content: center; gap: 6px;
  }
  .address {
    display: flex; align-items: center; gap: 20px;
    font-family: "Roboto", sans-serif; font-weight: 300; font-size: 25px; color: var(--white);
  }
  .address svg { width: 24px; height: 28px; flex: none; }
  .disclosure {
    font-family: "Roboto", sans-serif; font-weight: 300; font-size: 13px;
    letter-spacing: .5px; color: var(--muted);
  }
</style>
</head>
<body>

<section class="card card--front">
  <div class="front-photo" role="img" aria-label="Greyscale photo of several hands fitting puzzle pieces together"></div>
  <div class="brand brand--front"><span class="brand__dot"></span>Tallowbrook Partners</div>
  <p class="website">www.tallowbrookgroup.example</p>
</section>

<section class="card card--back">
  <div class="person">
    <h1 class="person__name">Dennis K. Holloway, MBA</h1>
    <p class="person__title">Founder/President</p>
  </div>

  <ul class="contacts">
    <li>
      <svg viewBox="0 0 24 24"><path d="M6.6 10.8a15.1 15.1 0 0 0 6.6 6.6l2.2-2.2a1 1 0 0 1 1-.25 11.4 11.4 0 0 0 3.6.57 1 1 0 0 1 1 1V20a1 1 0 0 1-1 1A17 17 0 0 1 3 4a1 1 0 0 1 1-1h3.5a1 1 0 0 1 1 1c0 1.25.2 2.450.57 3.57a1 1 0 0 1-.25 1z"/></svg>
      (402) 555-0147
    </li>
    <li>
      <svg viewBox="0 0 24 24"><path d="M7 1h10a2 2 0 0 1 2 2v18a2 2 0 0 1-2 2H7a2 2 0 0 1-2-2V3a2 2 0 0 1 2-2zm0 3v14h10V4zm5 15.3a1.2 1.2 0 1 0 0 2.4 1.2 1.2 0 0 0 0-2.4z"/></svg>
      (402) 555-0183
    </li>
    <li>
      <svg viewBox="0 0 24 24"><path d="M6 2h12v5H6zM3 8h18a2 2 0 0 1 2 2v7h-4v5H5v-5H1v-7a2 2 0 0 1 2-2zm4 8v4h10v-4zm1 1h8v1H8zm11-6.5a1 1 0 1 0 0 2 1 1 0 0 0 0-2z"/></svg>
      (402) 555-0129
    </li>
    <li>
      <svg viewBox="0 0 24 24"><path d="M2 5h20v14H2zm2 2v.5l8 5.5 8-5.5V7zm0 3v7h16v-7l-8 5.5z"/></svg>
      dennis@tallowbrookgroup.example
    </li>
  </ul>

  <div class="brand brand--back"><span class="brand__dot"></span>Tallowbrook Partners</div>

  <div class="address-band">
    <div class="address">
      <svg viewBox="0 0 24 28"><path d="M12 1.5a9 9 0 0 0-9 9c0 6.8 9 16 9 16s9-9.2 9-16a9 9 0 0 0-9-9z" fill="none" stroke="#fff" stroke-width="2.2"/><circle cx="12" cy="10.5" r="3.4" fill="none" stroke="#fff" stroke-width="2.2"/></svg>
      <span>5727 E. Larkspur Avenue Suite 418 Omaha, NE 68297</span>
    </div>
    <p class="disclosure">Advisory services offered through Marlowe Ridge Advisors, LLC</p>
  </div>
</section>

</body>
</html>
```